Medical Internet Marketing Company Needs a Site!

We need a new, fresh website for our search engine optimization and social media marketing company. We specialize in helping medical practices, doctors, physicians, and hospitals with their online presence and web ranking. The site should lean towards being suited for these audiences.

We have several examples of website that we like as well as things that we like about them.

Here are sites that we enjoy.

www.brightwavelab.com

It's a good design for the site all around. The videos, buttons, and images are all excellent. They did a fine job.

- We really like their "contact us" side bar and want to include one like it on the secondary pages.

www.corvantis.net

- We don't like the "thickness" of the top navigation bar.
- We like the page colors, easy navigation, and big call to action phone number in the top right corner.

http://www.teluvo.com/

Out of all the examples provided, Teluvo is our favorite and closest look and style to what we are looking for.

- We really like the openness of the design, such as space between the text and background.

- We want a price page in a style very similar to their pricing page with the services listed and check-marks, etc. although we intend to have multiple service package columns much like Corvantis's SEO pricing page.

- The way the video fits into the home page header is very organized, simple, and attention grabbing. We intend to place a slider with videos here.

- We need a page design that will allow for an image slider like Teluvo's Features page.

Here's a great example of a medical internet marketing website: http://www.dermaplex.com/

Target Market(s)

Our target market is doctors, typically male and typically 40-45 years old. I

Industry/Entity Type

Marketing

Requirements
Must have
• The homepage should have a slider in the video. Interior pages should have a video in the very top similar to how they do it on www.brightwavelab.com

The top navigation tabs needed are:
- Home
- Solutions
- Resources
- About
- Why Quelvo
- Contact

The sidebar should have a GREAT call to action in it on interior pages.

There should be one interior page that is similar to this - http://www.teluvo.com/pricing/

There needs to be a page with multiple boxes that take up a row of the web page's body. This page will house all the case studies similar to brightwave lab's: http://www.brightwavelab.com/success-stories/case-studies/ The one exception is we want the case studies to be inside of "boxes" instead of between horizontal lines like brightwave lab's.
Nice to have
• Color, professional, and clean. GREAT use of calls to actions.

```html
<!DOCTYPE html>
<html lang="en">
<head>
<meta charset="utf-8">
<title>Quelvo – Pricing</title>
<link href="https://fonts.googleapis.com/css2?family=Cabin:wght@400;500;600&display=swap" rel="stylesheet">
<style>
:root{
  --blue:#3b9ad0;
  --blue-text:#3a95c8;
  --green:#8cc63f;
  --yellow:#efb500;
  --grey-bg:#f1f1f1;
  --row:#e8e8e8;
  --text:#3c3c3c;
  --nav:#4a4a4a;
  --teal:#6cc6c4;
  --sky:#8cd3f0;
  --peach:#f2b26d;
  --leaf:#7fbf3a;
  --gold:#c9a200;
  --tick:#5cb84a;
  --cross:#e94b4b;
}
*{margin:0;padding:0;box-sizing:border-box}
html,body{width:1026px;height:1200px;overflow:hidden}
body{position:relative;font-family:'Cabin',sans-serif;color:var(--text);
  background:linear-gradient(to bottom,#f7f7f7 0,var(--grey-bg) 400px,var(--blue) 400px,var(--blue) 1079px,#000 1079px)}
.abs{position:absolute}
.brand{left:99px;top:22px;font-size:44px;letter-spacing:4px;color:#9a9a9a;font-weight:500}
.call{right:105px;top:28px;font-size:26px;color:var(--blue-text)}
.call span{color:var(--green)}
.rule{left:99px;top:85px;width:826px;height:1px;background:#dcdcdc}
.nav-marker{left:331px;top:84px}
.nav a{position:absolute;top:104px;font-size:15px;color:var(--nav);text-decoration:none;letter-spacing:.2px}
.support{left:991px;top:139px;width:35px;height:109px;background:var(--green);border-radius:4px 0 0 4px;
  color:#fff;font-size:16px;letter-spacing:1px;writing-mode:vertical-rl;transform:rotate(180deg);
  display:flex;align-items:center;justify-content:center}
.card{left:98px;top:139px;width:827px;height:897px;background:#fff;box-shadow:0 0 8px rgba(0,0,0,.08)}
.page-title{left:128px;top:162px;font-size:36px;font-weight:400;color:var(--blue-text)}
.promo{left:129px;top:215px;width:764px;height:116px;background:var(--yellow);padding:28px 0 0 24px}
.promo h2{font-size:27px;font-weight:400;color:#fff;line-height:30px}
.promo p{font-size:23px;color:#1f1f1f;line-height:28px}
.subhead{left:129px;top:355px;font-size:21px;font-weight:400;color:var(--green)}
.intro{left:129px;top:396px;width:764px;font-size:12.2px;line-height:18.8px;color:#333}
.plans{left:129px;top:501px;width:765px}
.tabs{display:grid;grid-template-columns:repeat(5,145px);column-gap:10px;height:62px}
.tab{position:relative;border-radius:4px 4px 0 0;color:#fff;font-size:15.5px;font-weight:500;
  line-height:19px;display:flex;align-items:center;padding-left:10px;gap:10px}
.tab::after{content:"";position:absolute;left:18px;bottom:-7px;border:7px solid transparent;border-bottom:0;border-top-color:inherit}
.tab .icon{width:34px;height:34px;border-radius:50%;background:rgba(255,255,255,.75);flex:none;display:flex;align-items:center;justify-content:center}
.t-feature{background:var(--teal);border-top-color:var(--teal)}
.t-self{background:var(--sky);border-top-color:var(--sky)}
.t-key{background:var(--peach);border-top-color:var(--peach)}
.t-small{background:var(--leaf);border-top-color:var(--leaf)}
.t-ent{background:var(--gold);border-top-color:var(--gold)}
.t-feature::after{border-top-color:var(--teal)}.t-self::after{border-top-color:var(--sky)}
.t-key::after{border-top-color:var(--peach)}.t-small::after{border-top-color:var(--leaf)}.t-ent::after{border-top-color:var(--gold)}
.row{display:grid;grid-template-columns:155px 155px 155px 155px 145px;height:43.6px;background:var(--row);
  border-bottom:1px solid #fff;align-items:center;font-size:12.6px;color:#444;line-height:15.5px}
.row:last-child{border-bottom:1px solid #d4d4d4}
.row .label{padding-left:21px;width:150px}
.row .c{display:flex;justify-content:center}
.row svg{width:14px;height:12px}
.foot a{position:absolute;font-size:11.5px;color:var(--blue);text-decoration:none}
.divider{width:1px;height:96px;top:1089px;background:#444}
.address{left:419px;top:1101px;font-size:11px;line-height:15.4px;color:#ddd}
.copy{right:98px;top:1096px;font-size:12px;color:#ddd}
.social{top:1122px;width:27px;height:27px;border-radius:50%;background:#555}
</style>
</head>
<body>
<svg width="0" height="0" class="abs" aria-hidden="true">
  <symbol id="tick" viewBox="0 0 14 12"><path d="M1 6.5l4 4L13 1.5" fill="none" stroke="#5cb84a" stroke-width="2.6" stroke-linecap="round" stroke-linejoin="round"/></symbol>
  <symbol id="cross" viewBox="0 0 14 12"><path d="M3 1.5l8 9M11 1.5l-8 9" fill="none" stroke="#e94b4b" stroke-width="2.6" stroke-linecap="round"/></symbol>
</svg>

<header>
  <div class="abs brand">QUELVO</div>
  <div class="abs call"><span>Call</span> 0987 654 321</div>
  <div class="abs rule"></div>
  <svg class="abs nav-marker" width="26" height="10" viewBox="0 0 26 10"><path d="M0 0h26L13 10z" fill="#f5a623"/></svg>
  <nav class="nav">
    <a style="left:121px">HOME</a>
    <a style="left:194px">WHY QUELVO</a>
    <a style="left:312px">PRICING</a>
    <a style="left:400px">SOLUTIONS</a>
    <a style="left:511px">FEATURES</a>
    <a style="left:609px">RESOURCES</a>
    <a style="left:719px">CASE STUDY</a>
    <a style="left:830px">CONTACT</a>
  </nav>
</header>

<div class="abs support">SUPPORT</div>

<main>
  <div class="abs card"></div>
  <h1 class="abs page-title">PRICING</h1>
  <section class="abs promo">
    <h2>FALL IN LOVE WITH QUELVO OR YOUR MONEY BACK</h2>
    <p>Search Engine Optimization plans run from as low as $99.00 a month</p>
  </section>
  <h3 class="abs subhead">NULLAM SOLLICITUDIN GRAVIDA MI SED PORTTITOR</h3>
  <p class="abs intro">Lorem ipsum dolor sit amet, consectetur adipiscing elit. Nullam sollicitudin gravida mi, sed porttitor erat blandit vel. Donec mattis est eu tortor convallis venenatis. Sed lectus justo, lobortis non pellentesque eget, egestas sit amet arcu. Etiam diam libero, egestas et tincidunt id, dictum non nisl. Ut velit lacus, accumsan eu molestie sit amet, gravida at augue. Nullam et semper risus. Cum sociis natoque penatibus et magnis dis parturient montes, nascetur ridiculus mus. Sed id ipsum fringilla metus iaculis iaculis eget sit amet nibh. Cum sociis natoque penatibus et magnis dis parturient montes, nascetur ridiculus mus. Phasellus porta vehicula fringilla.</p>

  <section class="abs plans">
    <div class="tabs">
      <div class="tab t-feature"><span class="icon"><svg width="18" height="14"><rect x="1" y="1" width="16" height="11" rx="1" fill="#333"/></svg></span>FEATURE</div>
      <div class="tab t-self"><span class="icon"><svg width="18" height="18"><circle cx="9" cy="9" r="6" fill="none" stroke="#333" stroke-width="3"/></svg></span>SELF<br>SERVICE</div>
      <div class="tab t-key"><span class="icon"><svg width="16" height="18"><rect x="1.5" y="1.5" width="13" height="15" rx="2" fill="none" stroke="#333" stroke-width="2"/><path d="M4 7h8M4 11h6" stroke="#333" stroke-width="1.6"/></svg></span>PER<br>KEYWORD</div>
      <div class="tab t-small"><span class="icon"><svg width="20" height="16"><rect x="1" y="4" width="18" height="11" rx="2" fill="none" stroke="#333" stroke-width="2"/><path d="M7 4V1.5h6V4" fill="none" stroke="#333" stroke-width="2"/></svg></span>SMALL<br>BUSINESS</div>
      <div class="tab t-ent"><span class="icon" role="img" aria-label="Enterprise client icon"></span>ENTERPRISE<br>SEO</div>
    </div>
    <div style="height:0"></div>
    <div class="row"><span class="label">Rank Tracking Reports</span><span class="c"><svg><use href="#tick"/></svg></span><span class="c"><svg><use href="#tick"/></svg></span><span class="c"><svg><use href="#tick"/></svg></span><span class="c"><svg><use href="#tick"/></svg></span></div>
    <div class="row"><span class="label">Track up to 100<br>Keywords</span><span class="c"><svg><use href="#tick"/></svg></span><span class="c"><svg><use href="#cross"/></svg></span><span class="c"><svg><use href="#tick"/></svg></span><span class="c"><svg><use href="#tick"/></svg></span></div>
    <div class="row"><span class="label">Track up to 200<br>Keywords</span><span class="c"><svg><use href="#tick"/></svg></span><span class="c"><svg><use href="#cross"/></svg></span><span class="c"><svg><use href="#cross"/></svg></span><span class="c"><svg><use href="#tick"/></svg></span></div>
    <div class="row"><span class="label">Track up to 50,000<br>Keywords</span><span class="c"><svg><use href="#tick"/></svg></span><span class="c"><svg><use href="#tick"/></svg></span><span class="c"><svg><use href="#tick"/></svg></span><span class="c"><svg><use href="#tick"/></svg></span></div>
    <div class="row"><span class="label">Rank Tracking<br>Reports</span><span class="c"><svg><use href="#tick"/></svg></span><span class="c"><svg><use href="#cross"/></svg></span><span class="c"><svg><use href="#tick"/></svg></span><span class="c"><svg><use href="#tick"/></svg></span></div>
    <div class="row"><span class="label">Track up to 100<br>Keywords</span><span class="c"><svg><use href="#tick"/></svg></span><span class="c"><svg><use href="#tick"/></svg></span><span class="c"><svg><use href="#tick"/></svg></span><span class="c"><svg><use href="#tick"/></svg></span></div>
    <div class="row"><span class="label">Unlimited SEO Page<br>Grader</span><span class="c"><svg><use href="#tick"/></svg></span><span class="c"><svg><use href="#cross"/></svg></span><span class="c"><svg><use href="#cross"/></svg></span><span class="c"><svg><use href="#tick"/></svg></span></div>
    <div class="row"><span class="label">Automated Site<br>Audit</span><span class="c"><svg><use href="#tick"/></svg></span><span class="c"><svg><use href="#cross"/></svg></span><span class="c"><svg><use href="#tick"/></svg></span><span class="c"><svg><use href="#tick"/></svg></span></div>
    <div class="row"><span class="label">Track up to 100<br>Keywords</span><span class="c"><svg><use href="#tick"/></svg></span><span class="c"><svg><use href="#cross"/></svg></span><span class="c"><svg><use href="#cross"/></svg></span><span class="c"><svg><use href="#cross"/></svg></span></div>
    <div class="row"><span class="label">Manual Site<br>Audit</span><span class="c"><svg><use href="#tick"/></svg></span><span class="c"><svg><use href="#cross"/></svg></span><span class="c"><svg><use href="#tick"/></svg></span><span class="c"><svg><use href="#tick"/></svg></span></div>
  </section>
</main>

<footer class="foot">
  <a style="left:101px;top:1099px">Why Quelvo</a>
  <a style="left:101px;top:1120px">pricing</a>
  <a style="left:101px;top:1140px">Solutions</a>
  <a style="left:101px;top:1161px">Features</a>
  <a style="left:221px;top:1099px">Resources</a>
  <a style="left:221px;top:1120px">Case Study</a>
  <a style="left:221px;top:1140px">About us</a>
  <div class="abs divider" style="left:349px"></div>
  <div class="abs divider" style="left:640px"></div>
  <address class="abs address" style="font-style:normal">QUELVO<br>Harbour Court, 4th floor<br>K L Road, Perth (East),<br>Australia<br>Phone: 0987 654 321</address>
  <div class="abs copy">Copyright © 2012 QUELVO. All right reserved.</div>
  <span class="abs social" style="left:773px" role="img" aria-label="Social link"></span>
  <span class="abs social" style="left:816px" role="img" aria-label="Social link"></span>
  <span class="abs social" style="left:859px" role="img" aria-label="Social link"></span>
  <span class="abs social" style="left:901px" role="img" aria-label="Social link"></span>
</footer>
</body>
</html>
```